Square graphic for social media post

I want to create a 1080 x 1080px all-black image for the quote below that I can share on social media. I want the emphasis to be primarily on the quote, secondarily on the portrait, and third (smallest) on the logo. I want the background on the portrait to be edited so it's transparent and just shows the face of the person on a black background (no brick wall visible).

Graphic color: black
Text color: white
Content: "What we went through is going to make the greatest generation of hoteliers our industry has ever seen." << biggest text
Derek Holloway << smaller text
President, Ridgemont Hotels << smaller text
[image of person - use whichever version looks better to you]
[Add Lodging Ledger logo - whichever looks better to you]

This image needs to be readable when sized down much smaller (400x400?) so want the text and portrait to take up most of the space.

I'd like the output both as PNG and original file (preferably Canva). Thanks!

Target Market(s)

Hotel managers

Industry/Entity Type

Hospitality

Font styles to use
Sans Serif

Colors

Designer to choose colors to be used in the design.

Requirements
Must have
• Needs to focus on the quote and the person quoted (the portrait)

```html
<!DOCTYPE html>
<html lang="en">
<head>
<meta charset="utf-8">
<title>Quote Post – Derek Holloway</title>
<link href="https://fonts.googleapis.com/css2?family=Lato:wght@400;700&display=swap" rel="stylesheet">
<style>
  :root {
    --bg: #000000;
    --text: #ffffff;
    --circle: #ffffff;
    --photo-dark: #2b3550;
    --photo-hair: #3a3634;
    --photo-mid: #b08f80;
    --photo-light: #d6b3a3;
  }
  html, body {
    margin: 0;
    padding: 0;
    width: 1200px;
    height: 1200px;
    overflow: hidden;
    background: var(--bg);
  }
  .post {
    position: relative;
    width: 1200px;
    height: 1200px;
    background: var(--bg);
    font-family: "Lato", Arial, sans-serif;
    color: var(--text);
    overflow: hidden;
  }
  .portrait-frame,
  .portrait-photo {
    position: absolute;
    left: 0;
    top: 0;
    width: 1200px;
    height: 1200px;
  }
  .quote-mark {
    position: absolute;
    font-weight: 700;
    font-size: 170px;
    line-height: 1;
  }
  .quote-mark--open { left: 116px; top: 76px; }
  .quote-mark--close { right: 90px; top: 492px; }
  .quote-text {
    position: absolute;
    right: 92px;
    top: 108px;
    width: 960px;
    margin: 0;
    text-align: right;
    font-weight: 700;
    font-size: 75px;
    line-height: 92px;
    letter-spacing: -0.5px;
  }
  .attribution {
    position: absolute;
    right: 90px;
    top: 614px;
    text-align: right;
  }
  .attribution__name {
    margin: 0;
    font-weight: 400;
    font-size: 60px;
    line-height: 72px;
    text-transform: uppercase;
    white-space: nowrap;
  }
  .attribution__role {
    margin: 4px 0 0;
    font-size: 48px;
    line-height: 56px;
  }
  .attribution__company {
    margin: 2px 0 0;
    font-size: 36px;
    line-height: 44px;
  }
  .brand {
    position: absolute;
    left: 800px;
    top: 975px;
    width: 300px;
    text-align: center;
    font-weight: 700;
    font-size: 30px;
    line-height: 40px;
    letter-spacing: 6px;
    text-transform: uppercase;
  }
</style>
</head>
<body>
  <main class="post">
    <svg class="portrait-frame" viewBox="0 0 1200 1200" aria-hidden="true">
      <circle cx="330" cy="1206" r="446" fill="none" stroke="var(--circle)" stroke-width="3"/>
      <circle cx="330" cy="1206" r="412" fill="var(--circle)"/>
    </svg>
    <svg class="portrait-photo" viewBox="0 0 1200 1200" role="img" aria-label="Head-and-shoulders portrait of Derek Holloway, smiling, in a navy blazer on a transparent background">
      <defs>
        <linearGradient id="portraitTone" x1="0" y1="0" x2="0" y2="1">
          <stop offset="0" stop-color="var(--photo-hair)"/>
          <stop offset="0.22" stop-color="var(--photo-hair)"/>
          <stop offset="0.35" stop-color="var(--photo-light)"/>
          <stop offset="0.7" stop-color="var(--photo-mid)"/>
          <stop offset="0.82" stop-color="var(--photo-dark)"/>
          <stop offset="1" stop-color="var(--photo-dark)"/>
        </linearGradient>
      </defs>
      <path fill="url(#portraitTone)" d="M0 1200 L0 1092 C60 1075 120 1050 150 1010 L150 980 C80 930 40 840 45 780 C40 650 150 565 276 565 C400 565 520 640 515 780 C515 860 470 940 410 985 L410 1020 C460 1060 560 1085 690 1100 L690 1200 Z"/>
    </svg>

    <span class="quote-mark quote-mark--open">“</span>
    <p class="quote-text">What we went through is going to make the greatest generation of hoteliers our industry has ever seen.</p>
    <span class="quote-mark quote-mark--close">”</span>

    <div class="attribution">
      <p class="attribution__name">Derek Holloway</p>
      <p class="attribution__role">President,</p>
      <p class="attribution__company">Ridgemont Hotels</p>
    </div>

    <div class="brand">Lodging<br>Ledger</div>
  </main>
</body>
</html>
```